Quorvel Landing page redesign

We are looking for a landing page redesign before we officially launch. We want to incorporate the information already on the site at www.Quorvel-example.com landing page but make it more inviting. There needs to be a sign up section along with clearly stating what we do. Having a place for sample profiles and linking to our blog and podcast is option. More information about all we will be doing is at Quorvel is on the landing page and also on the blog.

Target Market(s)

35 years old and up.

Coding

Coded - Design and coding required

Number of Pages Required

1 page

Requirements
Must have
• The top bar and the bottom bar (with the privacy policy, etc)
• Sign in/up section.
• I don't want to give to much here because I want designers to be creative.
Nice to have
• Prefer not to have a landing page that requires a lot of scrolling at all.

```html
<!DOCTYPE html>
<html lang="en">
<head>
<meta charset="utf-8">
<title>Quorvel</title>
<link rel="stylesheet" href="https://fonts.googleapis.com/css2?family=Lato:wght@400;700&family=Play:wght@400;700&display=swap">
<style>
:root{
  --dark:#2e2e2e;
  --blue:#1a8ad8;
  --blue-deep:#0f6fc0;
  --ink:#2b2b2b;
  --grey-band:#efefef;
  --white:#ffffff;
  --footer-link:#1b6fa8;
}
*{box-sizing:border-box;margin:0;padding:0}
html,body{width:890px;height:1200px;overflow:hidden;background:var(--white)}
body{position:relative;font-family:'Lato',sans-serif;color:var(--ink)}
.abs{position:absolute}
a{color:inherit;text-decoration:none}

.topbar{left:0;top:0;width:890px;height:36px;background:var(--dark)}
.toplinks{left:86px;top:12px;font-size:8px;color:var(--blue);white-space:nowrap}
.toplinks span.sep{color:#bbb;margin:0 4px}
.btn-sample{top:8px;height:22px;font-size:8px;font-weight:700;display:flex;align-items:center;justify-content:center;letter-spacing:-.1px}
.btn-sample.primary{left:564px;width:126px;background:var(--blue);color:var(--white)}
.btn-sample.secondary{left:696px;width:116px;background:var(--white);color:var(--ink)}

.header{left:0;top:36px;width:890px;height:62px;border-bottom:1px solid #eee;box-shadow:0 1px 3px rgba(0,0,0,.04)}
.brand-name{font-family:'Lato',sans-serif;font-size:21px;font-weight:400;white-space:nowrap}
.header .brand-name{left:86px;top:17px;color:var(--dark)}
.nav{top:24px;left:693px;font-family:'Lato',sans-serif;font-weight:700;font-size:13px;color:#444;display:flex;gap:29px}

.heading{left:0;width:890px;text-align:center;font-family:'Play',sans-serif;font-weight:700;font-size:30px;letter-spacing:2.5px;color:var(--ink)}
.sub{left:0;width:890px;text-align:center;font-family:'Play',sans-serif;font-weight:700;font-size:12.5px;letter-spacing:1.8px;line-height:18px;color:#333}

.rule{left:92px;top:237px;width:708px;height:1px;background:linear-gradient(90deg,transparent,#ddd 15%,#ddd 85%,transparent)}

.preview{left:90px;top:260px;width:396px;height:238px;background:var(--white);padding:7px;box-shadow:0 2px 5px rgba(0,0,0,.25);transform:rotate(-1.8deg)}
.preview div{width:100%;height:100%;background:linear-gradient(135deg,#47b4e8,#d9e4e8 45%,#47b4e8)}

.signin{left:531px;top:265px;width:279px;height:201px;background:#f1f1f1;border:1px solid #dcdcdc}
.signin-head{left:0;top:0;width:277px;height:65px;background:var(--dark);color:var(--white);text-align:center;font-family:'Play',sans-serif;font-weight:700;letter-spacing:1.8px}
.signin-head .t1{position:absolute;top:11px;width:100%;font-size:15px}
.signin-head .t2{position:absolute;top:36px;width:100%;font-size:12.5px}
.signin-head .t2 a{color:var(--blue)}
.notch{left:216px;top:65px;width:0;height:0;border-left:14px solid transparent;border-right:14px solid transparent;border-top:13px solid var(--dark)}
.field-label{left:16px;font-family:'Play',sans-serif;font-weight:700;font-size:12.5px;letter-spacing:1.6px;color:#333}
.field{left:100px;width:158px;height:18px;background:var(--white);border:1px solid #aaa}
.btn-blue{background:linear-gradient(#1e95e2,var(--blue-deep));color:var(--white);font-family:'Play',sans-serif;font-weight:700;letter-spacing:2px;display:flex;align-items:center;justify-content:center;border-radius:2px}
.signin .btn-blue{left:102px;top:151px;width:155px;height:35px;font-size:13px}
.sign-links{left:539px;top:474px;font-size:7.5px;color:var(--blue);white-space:nowrap}
.sign-links span.sep{color:#555;margin:0 5px}

.band{left:0;top:542px;width:890px;height:260px;background:var(--grey-band)}
.feature{width:150px;text-align:center;font-size:10.5px;line-height:16px;color:#555}
.feature b{color:#333;font-weight:700}
.feature svg{display:block;margin:0 auto 18px}

.early{left:92px;top:834px;width:710px;height:168px;border:2px solid #e6e6e6;border-radius:6px}
.early-text{left:0;top:908px;width:890px;text-align:center;font-family:'Lato',sans-serif;font-size:16.5px;color:#333}
.input{top:947px;height:33px;border:1px solid #ccc;border-radius:2px;display:flex;align-items:center;padding-left:12px;font-size:13px;color:#444;gap:9px}

.footer{left:0;top:1034px;width:890px;height:166px;background:var(--dark)}
.footer .brand-name{left:0;top:30px;width:890px;text-align:center;color:var(--white)}
.footer-rule{left:189px;top:87px;width:515px;height:1px;background:#888}
.footer-links{left:0;top:119px;width:890px;text-align:center;font-size:11.5px;color:var(--footer-link);word-spacing:1px}
.footer-links a{margin:0 2px}
</style>
</head>
<body>

<div class="abs topbar">
  <div class="abs toplinks"><a href="#">Privacy Policy</a><span class="sep">|</span><a href="#">Terms of Use</a><span class="sep">|</span><a href="#">Data Tracking Policy</a><span class="sep">|</span><a href="#">Submit Feedback</a></div>
  <a href="#" class="abs btn-sample primary">SAMPLE QUORVEL PROFILE</a>
  <a href="#" class="abs btn-sample secondary">SAMPLE LEGACY PROFILE</a>
</div>

<header class="abs header">
  <div class="abs brand-name">Quorvel</div>
  <nav class="abs nav"><a href="#">BLOG</a><a href="#">PODCAST</a></nav>
</header>

<h1 class="abs heading" style="top:133px">Quorvel Pages</h1>
<p class="abs sub" style="top:178px">Build multiple Quorvel pages through one account for yourself, your<br>family and to keep loved one's legacies alive.</p>
<div class="abs rule"></div>

<div class="abs preview"><div role="img" aria-label="Page preview showing a travel story card with a stadium photo over a map"></div></div>

<section class="abs signin">
  <div class="abs signin-head"><div class="t1">Quorvel Account</div><div class="t2">Sign In Here or <a href="#">Signup</a>?</div></div>
  <div class="abs notch"></div>
  <label class="abs field-label" style="top:88px">E-Mail</label>
  <div class="abs field" style="top:87px"></div>
  <label class="abs field-label" style="top:119px">Password</label>
  <div class="abs field" style="top:118px"></div>
  <a href="#" class="abs btn-blue">SIGN IN</a>
</section>
<div class="abs sign-links"><a href="#">Privacy Policy</a><span class="sep">|</span><a href="#">Terms of Use</a><span class="sep">|</span><a href="#">Data Tracking Policy</a><span class="sep">|</span><a href="#">Submit Feedback</a></div>

<section class="abs band"></section>
<h2 class="abs heading" style="top:576px">Why Choose Us</h2>
<p class="abs sub" style="top:621px">Build multiple Quorvel pages through one account</p>

<div class="abs feature" style="left:67px;top:672px">
  <svg width="40" height="40" viewBox="0 0 40 40"><circle cx="20" cy="20" r="18" fill="none" stroke="#1a8ad8" stroke-width="3"/><path d="M13 20l5 5 9-9" fill="none" stroke="#1a8ad8" stroke-width="3.2" stroke-linecap="round" stroke-linejoin="round"/></svg>
  <b>Create</b> Timelines, Maps,<br>Family Trees
</div>
<div class="abs feature" style="left:218px;top:672px">
  <svg width="40" height="40" viewBox="0 0 40 40"><circle cx="20" cy="20" r="18" fill="none" stroke="#1a8ad8" stroke-width="3"/><path d="M13 20l5 5 9-9" fill="none" stroke="#1a8ad8" stroke-width="3.2" stroke-linecap="round" stroke-linejoin="round"/></svg>
  <b>Share</b> Family Stories,<br>History and more
</div>
<div class="abs feature" style="left:369px;top:672px">
  <svg width="40" height="40" viewBox="0 0 40 40"><circle cx="20" cy="20" r="18" fill="none" stroke="#1a8ad8" stroke-width="3"/><path d="M13 20l5 5 9-9" fill="none" stroke="#1a8ad8" stroke-width="3.2" stroke-linecap="round" stroke-linejoin="round"/></svg>
  <b>Memorialize</b> Loved Ones
</div>
<div class="abs feature" style="left:530px;top:672px">
  <svg width="40" height="40" viewBox="0 0 40 40"><circle cx="20" cy="20" r="18" fill="none" stroke="#1a8ad8" stroke-width="3"/><path d="M13 20l5 5 9-9" fill="none" stroke="#1a8ad8" stroke-width="3.2" stroke-linecap="round" stroke-linejoin="round"/></svg>
  <b>Control</b> Your Privacy
</div>
<div class="abs feature" style="left:675px;top:672px">
  <svg width="40" height="40" viewBox="0 0 40 40"><circle cx="20" cy="20" r="18" fill="none" stroke="#1a8ad8" stroke-width="3"/><path d="M13 20l5 5 9-9" fill="none" stroke="#1a8ad8" stroke-width="3.2" stroke-linecap="round" stroke-linejoin="round"/></svg>
  <b>No Ads,</b> No Like Buttons<br>No News Feeds
</div>

<section class="abs early"></section>
<h2 class="abs heading" style="top:852px">Become An Early User</h2>
<p class="abs early-text">Signup now and receive an email once I publish new content.</p>
<div class="abs input" style="left:114px;width:252px">
  <svg width="16" height="16" viewBox="0 0 16 16"><circle cx="8" cy="5" r="3.5" fill="#aaa"/><path d="M1 16c0-4 3-6.5 7-6.5s7 2.5 7 6.5z" fill="#aaa"/></svg>Enter Your Name
</div>
<div class="abs input" style="left:380px;width:252px">
  <svg width="17" height="12" viewBox="0 0 17 12"><rect x=".5" y=".5" width="16" height="11" fill="none" stroke="#bbb"/><path d="M.5 .5l8 6 8-6" fill="none" stroke="#bbb"/></svg>Enter Your Email Address
</div>
<a href="#" class="abs btn-blue" style="left:646px;top:950px;width:133px;height:29px;font-size:12.5px">SIGN UP</a>

<footer class="abs footer">
  <div class="abs brand-name">Quorvel</div>
  <div class="abs footer-rule"></div>
  <div class="abs footer-links"><a href="#">Privacy Policy</a> <a href="#">Terms of Use</a> <a href="#">Data Tracking Policy</a> <a href="#">Submit Feedback</a> <a href="#">Quorvel © 2017</a></div>
</footer>

</body>
</html>
```